Packaging Design Project

THIS IS A PRODUCT THAT IS SOLD IN SMOKE SHOPS AND HEAD SHOPS IT IS CALLED GOLDEN MEADOW IT WILL BE SOLD IN A 2 DRAM BLUE BOTTLE WITH A SILVER CAP BELOW IN FILES IS A SAMPLE OF THE WORDING I NEED ON THE BOOTLE ALSO I NEED TO ADD SOMETHING LIKE POWERED BY KRATOM IS THE MAIN INGREDIENT
Updates
i uploade a picture of bootle thanks
Industry/Entity Type
Product
Look and feel
Each slider illustrates characteristics of the customer's brand and the style your logo design should communicate.

```html
<!DOCTYPE html>
<html lang="en">
<head>
<meta charset="utf-8">
<title>Golden Meadow – Vial Print Options</title>
<link href="https://fonts.googleapis.com/css2?family=Bangers&family=Michroma&display=swap" rel="stylesheet">
<style>
  :root {
    --page-bg: #ededed;
    --board-bg: #ffffff;
    --glass-blue: #2a2fd0;
    --glass-blue-deep: #1c1fa8;
    --print-white: #ffffff;
    --print-silver: #c9c9c9;
  }
  html, body {
    margin: 0;
    padding: 0;
    width: 949px;
    height: 1200px;
    overflow: hidden;
    background: var(--page-bg);
  }
  .sheet {
    position: relative;
    width: 949px;
    height: 1200px;
  }
  .option-board {
    position: absolute;
    left: 119px;
    width: 718px;
    height: 490px;
    background: var(--board-bg);
    box-shadow: 0 10px 40px rgba(0,0,0,0.12);
  }
  .option-board--white { top: 77px; --ink: var(--print-white); }
  .option-board--silver { top: 629px; --ink: var(--print-silver); }

  .print-panel {
    position: absolute;
    top: 105px;
    height: 321px;
    background: linear-gradient(90deg, var(--glass-blue-deep), var(--glass-blue) 35%, var(--glass-blue) 70%, var(--glass-blue-deep));
    border-radius: 6px;
  }
  .print-panel--front { left: 178px; width: 105px; }
  .print-panel--side { left: 329px; width: 98px; }

  .brand-block {
    position: absolute;
    top: 80px;
    left: 0;
    right: 0;
    text-align: center;
    color: var(--ink);
  }
  .brand-square {
    width: 40px;
    height: 40px;
    margin: 0 auto 12px;
    background: var(--ink);
  }
  .brand-name {
    font-family: "Bangers", "Impact", sans-serif;
    font-size: 30px;
    line-height: 0.95;
    letter-spacing: 0.5px;
    margin: 0;
  }
  .brand-descriptor {
    font-family: "Michroma", "Arial", sans-serif;
    font-size: 8px;
    line-height: 1.35;
    margin: 6px 0 0;
    letter-spacing: 0.3px;
  }
  .ingredient-line {
    position: absolute;
    top: 50%;
    left: 50%;
    transform: translate(-50%, -50%) rotate(-90deg);
    white-space: nowrap;
    font-family: "Bangers", "Impact", sans-serif;
    font-size: 30px;
    letter-spacing: 0.5px;
    color: var(--ink);
  }
</style>
</head>
<body>
<main class="sheet">
  <section class="option-board option-board--white" aria-label="White print option">
    <div class="print-panel print-panel--front">
      <div class="brand-block">
        <div class="brand-square"></div>
        <p class="brand-name">GOLDEN<br>MEADOW</p>
        <p class="brand-descriptor">LIQUID MOOD<br>ENHANCER</p>
      </div>
    </div>
    <div class="print-panel print-panel--side">
      <span class="ingredient-line">POWERED BY KRATOM</span>
    </div>
  </section>

  <section class="option-board option-board--silver" aria-label="Silver print option">
    <div class="print-panel print-panel--front">
      <div class="brand-block">
        <div class="brand-square"></div>
        <p class="brand-name">GOLDEN<br>MEADOW</p>
        <p class="brand-descriptor">LIQUID MOOD<br>ENHANCER</p>
      </div>
    </div>
    <div class="print-panel print-panel--side">
      <span class="ingredient-line">POWERED BY KRATOM</span>
    </div>
  </section>
</main>
</body>
</html>
```